Letterhead for new real estate company in South Africa named Tallowick

A letterhead with the directors and company details to be editable as these changes often

Target Market(s)

In line with our logo brief and our newly designed logo and corporate fee

Industry/Entity Type

Real Estate

Requirements
Must have
• Details as per the sample letterhead provided.

```html
<!DOCTYPE html>
<html lang="en">
<head>
<meta charset="utf-8">
<title>Tallowick Letterhead</title>
<link rel="stylesheet" href="https://fonts.googleapis.com/css2?family=Open+Sans:wght@400;600&family=Roboto:wght@400&display=swap">
<style>
  :root {
    --backdrop: #e4e4e4;
    --paper: #ffffff;
    --brand-green: #2fae6e;
    --brand-brown: #776a5e;
    --ink: #4a4a4a;
    --ink-soft: #5a5a5a;
    --signature-tone: #d9d9d9;
  }
  * { box-sizing: border-box; margin: 0; padding: 0; }
  html, body {
    width: 1200px; height: 800px; overflow: hidden;
    background: var(--backdrop);
  }
  .letterhead {
    position: absolute; left: 320px; top: 10px;
    width: 560px; height: 780px;
    background: var(--paper);
    box-shadow: 0 6px 20px rgba(0,0,0,0.12);
    font-family: "Open Sans", Arial, sans-serif;
    color: var(--ink);
  }
  .letterhead-header {
    position: absolute; left: 51px; right: 51px; top: 70px;
    display: flex; justify-content: space-between; align-items: flex-start;
  }
  .brand {
    display: flex; align-items: center; gap: 7px;
    margin-top: 4px;
  }
  .brand-dot {
    width: 12px; height: 12px; border-radius: 50%;
    background: var(--brand-green);
  }
  .brand-name {
    font-family: "Open Sans", Arial, sans-serif;
    font-weight: 400; font-size: 20px; letter-spacing: 0.3px;
    color: var(--brand-green); text-transform: uppercase;
  }
  .company-details {
    display: flex; gap: 12px;
    font-family: "Roboto", Arial, sans-serif;
    font-size: 9px; line-height: 11.5px; color: var(--ink-soft);
  }
  .company-address { text-align: right; }
  .contact-list { list-style: none; }
  .contact-list li { display: flex; align-items: center; gap: 4px; }
  .contact-icon { width: 8px; height: 8px; flex: none; }
  .letter-body {
    position: absolute; left: 51px; right: 51px; top: 165px;
    font-size: 10.4px; line-height: 15.1px;
  }
  .letter-body p { margin-bottom: 15px; text-align: justify; }
  .letter-body .salutation, .letter-body .closing { text-align: left; }
  .signature {
    position: absolute; left: 51px; top: 560px;
    width: 70px; height: 62px;
    background: linear-gradient(135deg, var(--paper), var(--signature-tone));
    border-radius: 4px;
  }
  .footer-bars {
    position: absolute; left: 0; right: 0; bottom: 0; height: 13px;
    display: flex; gap: 3px;
  }
  .footer-bar-green { width: 389px; background: var(--brand-green); }
  .footer-bar-brown { flex: 1; background: var(--brand-brown); }
</style>
</head>
<body>
  <article class="letterhead">
    <header class="letterhead-header">
      <div class="brand">
        <span class="brand-dot"></span>
        <span class="brand-name">Tallowick</span>
      </div>
      <div class="company-details">
        <address class="company-address" style="font-style:normal">
          Tallowick Property Professionals<br>
          14 Marram Lane<br>
          Kenwyn, Cape Town 7708
        </address>
        <ul class="contact-list">
          <li>
            <svg class="contact-icon" viewBox="0 0 8 8"><rect x="2" y="0.5" width="4" height="7" rx="0.8" fill="none" stroke="#2fae6e" stroke-width="0.9"/><circle cx="4" cy="6.2" r="0.45" fill="#2fae6e"/></svg>
            +27 21 555 0148
          </li>
          <li>
            <svg class="contact-icon" viewBox="0 0 8 8"><rect x="0.5" y="1.5" width="7" height="5" fill="#2fae6e"/><path d="M0.7 1.8 L4 4.4 L7.3 1.8" fill="none" stroke="#fff" stroke-width="0.7"/></svg>
            hello@tallowick.co.za
          </li>
          <li>
            <svg class="contact-icon" viewBox="0 0 8 8"><circle cx="4" cy="4" r="3.6" fill="#2fae6e"/><path d="M0.6 4 H7.4 M4 0.5 C2.4 2.5 2.4 5.5 4 7.5 M4 0.5 C5.6 2.5 5.6 5.5 4 7.5" fill="none" stroke="#fff" stroke-width="0.5"/></svg>
            www.tallowick.co.za
          </li>
        </ul>
      </div>
    </header>

    <section class="letter-body">
      <p class="salutation">Dear customer,</p>
      <p>Lorem ipsum dolor sit amet, consectetur adipisicing elit, sed do eiusmod tempor incididunt ut labore et dolore magna aliqua. Ut enim ad minim veniam, quis nostrud exercitation ullamco laboris nisi ut aliquip ex ea commodo consequat. Duis aute irure dolor in reprehenderit in voluptate velit esse cillum dolore eu fugiat nulla pariatur. Excepteur sint occaecat cupidatat non proident, sunt in culpa qui officia deserunt mollit anim id est laborum.</p>
      <p>Lorem ipsum dolor sit amet, consectetur adipisicing elit, sed do eiusmod tempor incididunt ut labore et dolore magna aliqua. Ut enim ad minim veniam, quis nostrud exercitation ullamco laboris nisi ut aliquip ex ea commodo consequat. Duis aute irure dolor in reprehenderit in voluptate velit esse cillum dolore eu fugiat nulla pariatur. Excepteur sint occaecat cupidatat non proident, sunt in culpa qui officia deserunt mollit anim id est laborum.</p>
      <p>Lorem ipsum dolor sit amet, consectetur adipisicing elit, sed do eiusmod tempor incididunt ut labore et dolore magna aliqua. Ut enim ad minim veniam, quis nostrud exercitation ullamco laboris nisi ut aliquip ex ea commodo consequat. Duis aute irure dolor in reprehenderit in voluptate velit esse cillum dolore eu fugiat nulla pariatur. Excepteur sint occaecat cupidatat non proident, sunt in culpa qui officia deserunt mollit anim id est laborum.</p>
      <p>Lorem ipsum dolor sit amet, consectetur adipisicing elit, sed do eiusmod tempor incididunt ut labore et dolore magna aliqua. Ut enim ad minim veniam, quis nostrud exercitation ullamco laboris nisi ut aliquip ex ea commodo consequat. Duis aute irure dolor in reprehenderit.</p>
      <p class="closing">Yours Sincerely,</p>
    </section>

    <div class="signature" role="img" aria-label="Handwritten signature of the sender"></div>

    <footer class="footer-bars">
      <div class="footer-bar-green"></div>
      <div class="footer-bar-brown"></div>
    </footer>
  </article>
</body>
</html>
```